Construction Company Stationary Design

We have previously utilised Artelvo to develop a new logo, we wanted to implement it for a while to ensure we liked it before rolling out new stationary. The time has come and we require:
Business Cards
"With Compliments" Cards
Asset Stickers
Vehicle Stickers
Letterhead
Document Header
Invoice Header
Cover Page
We are an established Construction Company working in Northern Australia (outback) that is venturing into a more corporate environment. We DO NOT do residential construction, we focus on commercial & government (Defence, schools, health etc) and work in both urban and remote environments.
Business Card Requirements:
• Logo
• Company Name
• Staff Name
• Staff Position
• Company Physical & Postal Address
• ABN
• Staff Mobile
• Staff Direct Phone (if applicable)
• Staff Email
• Office Phone
• Office Fax
"With Compliments" cards to be much the same as the business cards but with company details only (no staff details)
Asset stickers again to be much the same but with a space to write in asset number.
Document header requires 4 spaces to enter details much like our previous one attached.
We appreciate that designers time is valuable and would request that samples only be produced for one or two of the required items (say Business Card & Letterhead) and await a feedback score of 4 or more prior to producing the full suite of stationary.
If you require any further information please do not hesitate to contact me. colin@brevmark.com.au
Construction

```html
<!DOCTYPE html>
<html lang="en">
<head>
<meta charset="UTF-8">
<title>Brenhurst Constructions – Business Card</title>
<link href="https://fonts.googleapis.com/css2?family=Oswald:wght@600&family=Open+Sans:wght@400;600&display=swap" rel="stylesheet">
<style>
  :root {
    --page-bg: #e9e7e4;
    --card-black: #151515;
    --card-black-soft: #2a2a2a;
    --card-white: #ffffff;
    --brand-orange: #f05a28;
    --text-light: #f2f2f2;
    --text-muted: #bdbdbd;
    --text-dark: #1b1b1b;
  }
  * { box-sizing: border-box; margin: 0; padding: 0; }
  html, body { width: 1200px; height: 1024px; overflow: hidden; }
  body {
    background: var(--page-bg);
    font-family: "Open Sans", Arial, sans-serif;
    position: relative;
  }
  .card {
    position: absolute;
    width: 630px;
    height: 360px;
    border-radius: 26px;
    overflow: hidden;
    box-shadow: 0 10px 28px rgba(0,0,0,0.22);
  }
  /* ---------- front ---------- */
  .card-front { left: 285px; top: 90px; background: var(--card-black); }
  .front-white {
    position: absolute; left: 0; top: 0; width: 100%; height: 150px;
    background: var(--card-white);
  }
  .front-black-step {
    position: absolute; left: 360px; top: 108px; width: 270px; height: 80px;
    background: var(--card-black);
    border-top-left-radius: 34px;
    border-top: 4px solid var(--brand-orange);
  }
  .front-orange-band {
    position: absolute; left: 0; top: 150px; width: 360px; height: 62px;
    background: var(--brand-orange);
    padding: 8px 0 0 34px;
  }
  .front-orange-band::after {
    content: ""; position: absolute; right: -34px; top: 0; width: 34px; height: 62px;
    background: var(--brand-orange);
  }
  .staff-name { color: #fff; font-size: 21px; font-weight: 400; line-height: 1.2; }
  .staff-role { color: #fff; font-size: 13px; line-height: 1.2; }
  .front-logo {
    position: absolute; left: 34px; top: 34px;
    display: flex; align-items: center; gap: 14px;
  }
  .logo-square { width: 34px; height: 34px; background: var(--brand-orange); }
  .logo-name {
    font-family: "Oswald", Arial, sans-serif; font-weight: 600;
    font-size: 30px; letter-spacing: 1px; line-height: 1.1;
    text-transform: uppercase; color: var(--text-dark);
  }
  .address {
    position: absolute; left: 34px; top: 244px;
    color: var(--text-light); font-size: 13.5px; line-height: 1.55;
  }
  .contact-list { position: absolute; list-style: none; color: var(--text-light); font-size: 13.5px; line-height: 1.6; }
  .contact-list li { display: flex; align-items: center; gap: 9px; }
  .contact-list svg { width: 13px; height: 13px; fill: var(--brand-orange); flex: none; }
  .phones { left: 262px; top: 232px; }
  .online { left: 440px; top: 232px; }
  /* ---------- back ---------- */
  .card-back {
    left: 285px; top: 540px;
    background: radial-gradient(ellipse at 40% 30%, var(--card-black-soft) 0%, var(--card-black) 70%);
  }
  .back-logo {
    position: absolute; left: 0; top: 120px; width: 100%;
    display: flex; justify-content: center; align-items: center; gap: 18px;
  }
  .back-logo .logo-name { color: #fff; font-size: 40px; }
  .back-logo .logo-square { width: 44px; height: 44px; }
  .back-web {
    position: absolute; left: 0; bottom: 44px; width: 100%;
    text-align: center; color: var(--text-muted); font-size: 14px;
  }
</style>
</head>
<body>

<section class="card card-front" aria-label="Business card front">
  <div class="front-white"></div>
  <div class="front-black-step"></div>
  <div class="front-logo">
    <span class="logo-square"></span>
    <span class="logo-name">Brenhurst Constructions</span>
  </div>
  <div class="front-orange-band">
    <p class="staff-name">Daniel Rourke</p>
    <p class="staff-role">Company Manager</p>
  </div>
  <p class="address">Suite 204<br>17 Harlan Street<br>Darwin NT 0800</p>
  <ul class="contact-list phones">
    <li><svg viewBox="0 0 16 16"><path d="M3 1h3l1.5 4-2 1.2a9 9 0 0 0 4.3 4.3L11 8.5l4 1.5v3a2 2 0 0 1-2 2A12 12 0 0 1 1 3a2 2 0 0 1 2-2z"/></svg>555-0142-2381</li>
    <li><svg viewBox="0 0 16 16"><path d="M4 0h8a1 1 0 0 1 1 1v14a1 1 0 0 1-1 1H4a1 1 0 0 1-1-1V1a1 1 0 0 1 1-1zm1 2v10h6V2z"/></svg>555-0178-6490</li>
    <li><svg viewBox="0 0 16 16"><path d="M4 1h7v4H4zM2 6h12a1 1 0 0 1 1 1v6H1V7a1 1 0 0 1 1-1zm2 8h8v2H4z"/></svg>555-0193-5127</li>
  </ul>
  <ul class="contact-list online">
    <li><svg viewBox="0 0 16 16"><path d="M3 1h3l1.5 4-2 1.2a9 9 0 0 0 4.3 4.3L11 8.5l4 1.5v3a2 2 0 0 1-2 2A12 12 0 0 1 1 3a2 2 0 0 1 2-2z"/></svg>555-0126-7734</li>
    <li><svg viewBox="0 0 16 16"><path d="M1 3h14v10H1zm1.5 1.5v.4L8 9l5.5-4.1v-.4z"/></svg>office@brenhurst.com.au</li>
    <li><svg viewBox="0 0 16 16"><circle cx="8" cy="8" r="7"/></svg>www.brenhurst.com.au</li>
  </ul>
</section>

<section class="card card-back" aria-label="Business card back">
  <div class="back-logo">
    <span class="logo-square"></span>
    <span class="logo-name">Brenhurst Constructions</span>
  </div>
  <p class="back-web">www.brenhurstconstructions.com</p>
</section>

</body>
</html>
```